Realtor needs 8 1/2 x 11 flyer designed both sides

I uploaded a new word doc to be used under each of the pictures on the front page.

Colors

Designer to choose colors to be used in the design.

```html
<!DOCTYPE html>
<html lang="en">
<head>
<meta charset="utf-8">
<title>Why Choose Us – Flyer</title>
<link href="https://fonts.googleapis.com/css2?family=Gelasio:wght@700&family=PT+Sans:wght@400&family=Arimo:wght@400&display=swap" rel="stylesheet">
<style>
  :root{
    --brand-blue:#1a4494;
    --page:#f3f3f4;
    --backdrop:#e6e6e8;
    --panel-grey:#c9c9cb;
    --ink:#1b1b1b;
    --white:#ffffff;
    --photo-warm:#8a6b55;
    --photo-cool:#b9b4ae;
  }
  *{margin:0;padding:0;box-sizing:border-box}
  html,body{width:1179px;height:1200px;overflow:hidden;background:var(--backdrop)}
  .flyer{position:absolute;left:132px;top:0;width:914px;height:1200px;background:var(--page);font-family:"PT Sans",sans-serif;color:var(--ink)}
  .abs{position:absolute}
  .portrait{display:block}
  .portrait--laura{left:98px;top:93px;width:242px;height:327px}
  .portrait--marta{left:428px;top:420px;width:432px;height:247px}
  .accent-bar{left:59px;top:420px;width:346px;height:19px;background:var(--brand-blue)}
  .headline{right:80px;top:118px;text-align:right;font-family:"Gelasio",serif;font-weight:700;color:var(--brand-blue);font-size:100px;line-height:90px;letter-spacing:-1px}
  .note-title{font-family:"Gelasio",serif;font-weight:700;text-align:center}
  .note-title--laura{left:59px;width:346px;top:446px;font-size:31px;color:var(--brand-blue)}
  .note-title--marta{left:428px;width:432px;top:686px;font-size:34px;color:var(--ink)}
  .note{font-size:12.2px;line-height:16.4px;text-align:justify;hyphens:auto}
  .note p+p{margin-top:16px}
  .note--laura{left:60px;top:499px;width:343px;height:362px;background:var(--brand-blue);color:var(--white);padding:14px 22px}
  .note--marta{left:428px;top:736px;width:432px;height:352px;background:var(--panel-grey);color:var(--ink);padding:18px 24px;font-size:11.8px;line-height:16.3px}
  .contacts{right:512px;text-align:right;font-family:"Arimo",sans-serif;font-size:14px;line-height:18px}
  .contacts .name{font-family:"Gelasio",serif;font-weight:700;font-size:27px;line-height:32px;margin-bottom:4px}
  .contacts--laura{top:883px}
  .contacts--marta{top:993px}
</style>
</head>
<body>
<main class="flyer">
  <svg class="abs portrait portrait--laura" role="img" aria-label="Portrait photo of realtor Laura Bennett" viewBox="0 0 242 327" preserveAspectRatio="none">
    <defs><linearGradient id="lauraTone" x1="0" y1="0" x2="0" y2="1"><stop offset="0" stop-color="#e7d9b8"/><stop offset="0.6" stop-color="#cfb28c"/><stop offset="1" stop-color="#2a2a2e"/></linearGradient></defs>
    <rect width="242" height="327" fill="url(#lauraTone)"/>
  </svg>
  <div class="abs accent-bar"></div>

  <h1 class="abs headline">WHY<br>CHOOSE<br>US?</h1>

  <h2 class="abs note-title note-title--laura">A note from Laura</h2>
  <div class="abs note note--laura">
    <p>I know many of you, but for those whom I do not, I'd like to introduce myself. I've been a resident of Harbor Crest for almost 23 years now. I've loved our neighborhood from the first time I discovered it. From our beautiful parks to our fabulous pool and amenities, it's hard to beat our wonderful community. I always say where we live is the next best thing to living on a tropical island. I've traveled to many places and I'm always happy to come back to my Harbor Crest home. My passion for this area is why I'm in Real Estate. I consider myself incredibly lucky to sell homes in an area that I love with all my heart.</p>
    <p>Marta and I have been close colleagues for the last 8 years, both working as Realtors and long time residents of Harbor Crest. I am most grateful for our working relationship and the friendship we have formed. I am humbled by her trust and respect for me. Please feel welcome to call on me for all things home-related. I will look forward to meeting you!</p>
  </div>

  <svg class="abs portrait portrait--marta" role="img" aria-label="Photo of realtor Marta Sloane in her home" viewBox="0 0 432 247" preserveAspectRatio="none">
    <defs><linearGradient id="martaTone" x1="0" y1="0" x2="1" y2="1"><stop offset="0" stop-color="#6f5a45"/><stop offset="0.5" stop-color="#c9a982"/><stop offset="1" stop-color="#8d8a86"/></linearGradient></defs>
    <rect width="432" height="247" fill="url(#martaTone)"/>
  </svg>

  <h2 class="abs note-title note-title--marta">A note from Marta</h2>
  <div class="abs note note--marta">
    <p>I have exciting and bittersweet news I want to share with my Harbor Crest clients, friends and neighbors. After 40 years in the Real Estate business, I have decided to retire. Some of you may know that last month I sold my Harbor Crest home and moved to the beautiful Willow Glen community in Cedar Valley. My husband and I wanted to scale down and have time to enjoy retirement, together. I have been so blessed to have had a wonderful career in Real Estate and I want to thank you with a most grateful heart for giving me the opportunity to work with you. I have enjoyed every minute.</p>
    <p>I'm happy and proud to be turning my business over to Laura Bennett, fellow Summit Realty agent. She and I have enjoyed a very close working relationship for many years and there is nobody else except Laura I'd consider turning my business over to. Laura is caring, honest and truly tireless for her clients. Please contact me if you'd like a personal introduction to Laura or contact her directly. Remember to mention me when you contact Laura and let her know that we know each other. I wish you the very best and please say hello when you see me in the neighborhood.</p>
  </div>

  <address class="abs contacts contacts--laura" style="font-style:normal">
    <div class="name">Laura Bennett</div>
    555.214.3380<br>
    Realtor &nbsp;|&nbsp; DRE# 01234567<br>
    Laura@LauraBennettHomes.com
  </address>
  <address class="abs contacts contacts--marta" style="font-style:normal">
    <div class="name">Marta Sloane</div>
    Realtor<br>
    555.407.1926 &nbsp;|&nbsp; DRE# 00765432<br>
    Marta@MartaSloane.com
  </address>
</main>
</body>
</html>
```